Flyer-Design für  Kampfsportschule
Flyer-Design für Kampfsportschule
Zielgruppe
Wir bieten Taekwondo/Selbstverteidigung an. Meine Zielgruppe sind Erwachsene ab 17 Jahren.
Aufgabenstellung
Das Angebot '1 Monat kostenloses Training, oder einen Monat kostenloses Training' und 'Taekwondo/Selbstverteidigung in Weinstadt' soll eingebracht und direkt sichtbar sein. Eventuell auch Punkte wie Selbstbewusstsein, Beweglichkeit, Zielstrebigkeit, Kraft und Ausdauer, körperliche Fitness... Farben: Weiß, schwarz und Schrift in gelb. Nichts rotes.
Die Daten:
Tel: 0159-4817250 Email: t.m.budohalle@postwelle-mail.de und www.tmbudohalle.de

```html
<!DOCTYPE html>
<html lang="de">
<head>
<meta charset="utf-8">
<title>Flyer – T.M. Budohalle</title>
<link href="https://fonts.googleapis.com/css2?family=Fira+Sans:wght@800&family=Fira+Sans+Condensed:wght@800&family=Fira+Sans+Extra+Condensed:ital,wght@1,900&family=Open+Sans:wght@400&display=swap" rel="stylesheet">
<style>
  :root {
    --paper: #ffffff;
    --ink: #1e1e1e;
    --night: #1c1b1a;
    --gold: #fbb829;
    --white: #ffffff;
    --backdrop: #f2f2f2;
    --photo-light: #eceef0;
    --photo-mid: #c9cdd2;
  }
  * { margin: 0; padding: 0; box-sizing: border-box; }
  html, body { width: 1195px; height: 1200px; overflow: hidden; background: var(--backdrop); }
  .flyer {
    position: absolute; left: 240px; top: 116px;
    width: 715px; height: 968px;
    background: var(--paper); overflow: hidden;
  }
  .hero-photo {
    position: absolute; left: 0; top: 150px; width: 715px; height: 420px;
    background: linear-gradient(160deg, var(--photo-light) 0%, var(--photo-mid) 55%, #9aa0a6 100%);
  }
  .dark-band { position: absolute; left: 0; top: 0; width: 715px; height: 968px; }
  .intro {
    position: absolute; top: 40px; width: 100%; text-align: center;
    font-family: "Fira Sans", sans-serif; font-weight: 800;
    font-size: 25px; color: var(--ink);
  }
  .intro-big {
    position: absolute; top: 68px; width: 100%; text-align: center;
    font-family: "Fira Sans", sans-serif; font-weight: 800;
    font-size: 48px; color: var(--gold); line-height: 1;
  }
  .offer {
    position: absolute; font-family: "Fira Sans Extra Condensed", sans-serif;
    font-style: italic; font-weight: 900; line-height: 1; white-space: nowrap;
    transform: rotate(-10deg); transform-origin: left bottom;
  }
  .offer-month { left: 20px; top: 365px; font-size: 128px; color: var(--white); }
  .offer-free { left: 72px; top: 505px; font-size: 110px; color: var(--gold); }
  .phone {
    position: absolute; left: 240px; top: 600px; display: flex; align-items: center; gap: 8px;
    transform: rotate(-10deg); transform-origin: left center;
    font-family: "Fira Sans", sans-serif; font-weight: 800; font-size: 36px; color: var(--white);
  }
  .brand {
    position: absolute; left: 50px; top: 668px; width: 186px; height: 186px;
    border-radius: 50%; background: var(--white);
    display: flex; align-items: center; justify-content: center; text-align: center;
    font-family: "Fira Sans Condensed", sans-serif; font-weight: 800;
    font-size: 26px; line-height: 1.1; color: var(--ink);
  }
  .benefits {
    position: absolute; left: 266px; top: 680px; list-style: none;
    font-family: "Fira Sans Condensed", sans-serif; font-weight: 800;
    font-size: 21px; color: var(--gold);
  }
  .benefits li { position: relative; padding-left: 34px; height: 33px; line-height: 33px; }
  .benefits li::before {
    content: ""; position: absolute; left: 0; top: 10px;
    width: 13px; height: 13px; border-radius: 50%; background: var(--gold);
  }
  .location {
    position: absolute; top: 870px; width: 100%; text-align: center;
    font-family: "Fira Sans Condensed", sans-serif; font-weight: 800;
    font-size: 22px; color: var(--gold); letter-spacing: 0.5px;
  }
  .contact {
    position: absolute; top: 914px; width: 100%; display: flex; justify-content: center; gap: 18px;
    font-family: "Open Sans", sans-serif; font-size: 17px; color: var(--white);
  }
  .contact span { display: flex; align-items: center; gap: 7px; }
</style>
</head>
<body>
  <main class="flyer">
    <div class="hero-photo" role="img" aria-label="Foto eines Kampfsportlers im weißen Anzug beim Sprungtritt durch zerrissenes Papier vor Stadtkulisse"></div>

    <svg class="dark-band" viewBox="0 0 715 968" aria-hidden="true">
      <polygon points="0,545 715,328 715,968 0,968" fill="var(--night)"/>
    </svg>

    <p class="intro">Komm in unser Team und</p>
    <p class="intro-big">Trainiere mit uns</p>

    <p class="offer offer-month">1 MONAT</p>
    <p class="offer offer-free">KOSTENLOS!</p>

    <p class="phone">
      <svg width="26" height="30" viewBox="0 0 24 24" aria-hidden="true">
        <path fill="var(--gold)" d="M6.6 10.8a15 15 0 0 0 6.6 6.6l2.2-2.2c.3-.3.7-.4 1-.2 1.1.4 2.3.6 3.6.6.6 0 1 .4 1 1V20c0 .6-.4 1-1 1A17 17 0 0 1 3 4c0-.6.4-1 1-1h3.5c.6 0 1 .4 1 1 0 1.3.2 2.5.6 3.6.1.3 0 .7-.2 1z"/>
      </svg>
      0159-4817250
    </p>

    <div class="brand">T.M.<br>Budohalle</div>

    <ul class="benefits">
      <li>Selbstbewusstsein,</li>
      <li>Beweglichkeit, Zielstrebigkeit,</li>
      <li>Kraft und Ausdauer,</li>
      <li>körperliche Fitness</li>
    </ul>

    <p class="location">Taekwondo/Selbstverteidigung \ in Weinstadt</p>

    <div class="contact">
      <span>
        <svg width="24" height="18" viewBox="0 0 24 18" aria-hidden="true">
          <rect x="0" y="0" width="24" height="18" fill="var(--gold)"/>
          <path d="M1 1l11 9 11-9" fill="none" stroke="var(--night)" stroke-width="2"/>
        </svg>
        t.m.budohalle@postwelle-mail.de
      </span>
      <span>
        <svg width="22" height="22" viewBox="0 0 24 24" aria-hidden="true">
          <g fill="none" stroke="var(--gold)" stroke-width="2">
            <circle cx="12" cy="12" r="10"/>
            <ellipse cx="12" cy="12" rx="4.5" ry="10"/>
            <line x1="2" y1="12" x2="22" y2="12"/>
            <line x1="4" y1="6.5" x2="20" y2="6.5"/>
            <line x1="4" y1="17.5" x2="20" y2="17.5"/>
          </g>
        </svg>
        www.tmbudohalle.de
      </span>
    </div>
  </main>
</body>
</html>
```